Coastal Gin Label Design

We are needing a nautical/coastal themed label for our upcoming gin release.

We have saltbush, cucumber, juniper, and quandong being used in this gin.

Name of the Gin; Harbor Glow

The logo attached is the company logo, but doesn't have to be used on the front of the label, ie it can just be the name Fernwhistle somewhere on the front.
Bottle specs attached as well so you can accurately represent the bottle- this bottle is also clear.

Target Market(s)

Women 25- 45

Font styles to use
Serif
Decorative

Colors
d5edf4
86cae7
33a6d7
86cfc6
cfeae6
ffffff
f6faec
ecf7fb
fefeff

Requirements
Must have
• Ocean/Coastal vibe to the label
Nice to have
• Blues,Whites clean and crisp
Should not have
• No generic word art look to it.
A dark mood

```html
<!DOCTYPE html>
<html lang="en">
<head>
<meta charset="utf-8">
<title>Harbor Glow – Australian Coastal Gin Label</title>
<link rel="stylesheet" href="https://fonts.googleapis.com/css2?family=Yeseva+One&family=Oswald:wght@300;500&family=Poppins:wght@300;500&display=swap">
<style>
  :root {
    --page: #ffffff;
    --sea-blue: #31b8d8;
    --sea-light: #5fcbe2;
    --sea-pale: #86d6e4;
    --foam: #ffffff;
    --foam-shade: #eef3f2;
    --sand-light: #d9ad6b;
    --sand: #c99552;
    --sand-deep: #a8713a;
    --band: #9a5424;
    --ink-navy: #0b5a92;
    --ink-white: #ffffff;
  }
  * { margin: 0; padding: 0; box-sizing: border-box; }
  html, body {
    width: 949px;
    height: 1200px;
    overflow: hidden;
    background: var(--page);
  }
  .canvas {
    position: relative;
    width: 949px;
    height: 1200px;
  }
  .label {
    position: absolute;
    left: 183px;
    top: 60px;
    width: 583px;
    height: 1081px;
    border-radius: 291px 291px 6px 6px / 286px 286px 6px 6px;
    background: var(--sea-blue);
    overflow: hidden;
  }
  .shoreline-art {
    position: absolute;
    left: 0;
    top: 400px;
    width: 100%;
    height: 636px;
    background: linear-gradient(180deg,
      var(--sea-blue) 0%,
      var(--sea-light) 12%,
      var(--sea-pale) 26%,
      var(--foam) 38%,
      var(--foam-shade) 47%,
      var(--sand-light) 55%,
      var(--sand) 72%,
      var(--sand-light) 88%,
      var(--sand-deep) 100%);
  }
  .product-name {
    position: absolute;
    left: 0;
    top: 190px;
    width: 100%;
    font-family: "Yeseva One", serif;
    color: var(--ink-white);
    text-shadow: 0 4px 8px rgba(0, 60, 90, 0.25);
    line-height: 1;
  }
  .product-name .line-one {
    display: block;
    font-size: 112px;
    text-align: center;
    letter-spacing: -1px;
  }
  .product-name .line-two {
    display: block;
    font-size: 104px;
    padding-left: 215px;
    margin-top: -8px;
  }
  .spirit-type {
    position: absolute;
    right: 154px;
    top: 430px;
    display: flex;
    align-items: center;
    gap: 10px;
    color: var(--ink-navy);
  }
  .spirit-type .origin {
    font-family: "Oswald", sans-serif;
    font-weight: 500;
    font-size: 29px;
    line-height: 1.1;
    text-align: right;
    text-transform: uppercase;
    letter-spacing: -0.5px;
  }
  .spirit-type .category {
    font-family: "Oswald", sans-serif;
    font-weight: 300;
    font-size: 74px;
    line-height: 1;
  }
  .maker {
    position: absolute;
    left: 0;
    top: 938px;
    width: 100%;
    text-align: center;
    font-family: "Poppins", sans-serif;
    color: var(--ink-white);
    text-shadow: 0 2px 5px rgba(80, 45, 10, 0.35);
  }
  .maker .lead {
    display: block;
    font-weight: 500;
    font-size: 20px;
    line-height: 1.2;
  }
  .maker .distillery {
    display: block;
    font-weight: 300;
    font-size: 32px;
    line-height: 1.3;
    letter-spacing: 0.5px;
  }
  .volume-band {
    position: absolute;
    left: 0;
    bottom: 0;
    width: 100%;
    height: 45px;
    background: var(--band);
    color: var(--ink-white);
    font-family: "Poppins", sans-serif;
    font-weight: 500;
    font-size: 22px;
    line-height: 45px;
    text-align: center;
  }
</style>
</head>
<body>
  <main class="canvas">
    <section class="label">
      <div class="shoreline-art" role="img" aria-label="Illustration of turquoise ocean water washing onto a sandy beach with white sea foam"></div>
      <h1 class="product-name">
        <span class="line-one">Harbor</span>
        <span class="line-two">Glow</span>
      </h1>
      <div class="spirit-type">
        <p class="origin">Australian<br>Coastal</p>
        <p class="category">GIN</p>
      </div>
      <p class="maker">
        <span class="lead">Distilled by</span>
        <span class="distillery">Fernwhistle</span>
      </p>
      <p class="volume-band">500 ml</p>
    </section>
  </main>
</body>
</html>
```